Real Estate Valuation Services

format
A5 portrait, look at the picture
Double-sided: Front = visual & emotional, Back = informative & structured.
goal
Highlight the free hedonic property valuation as the main offer.
Build trust by presenting the company as an exclusive, family-owned real estate firm with local roots in Meilen/ZH.
Communicate the USP “Everything from one source” clearly – from valuation to notary support and tax guidance.
Target audience
Homeowners in the Lake Zurich region considering selling their property.
Clients who value exclusivity, professionalism, and personal service.
Design style
Modern, clean, elegant – plenty of white space. Look at the website: https://lindtaberhaus.ch/
Tone: Professional, trustworthy, exclusive – not like a mass-market flyer.
If possible, the text should be in German. Contact details must be included:
info@lindtaberhaus.ch
+41 77 586 12 47
Target Market(s)
property owner
Industry/Entity Type
real estate
Look and feel
Each slider illustrates characteristics of the customer's brand and the style your logo design should communicate.

```html
<!DOCTYPE html>
<html lang="de">
<head>
<meta charset="utf-8">
<title>Lindtaber Immobilien – Flyer</title>
<link href="https://fonts.googleapis.com/css2?family=Montserrat:wght@400;500;600;700&display=swap" rel="stylesheet">
<style>
  :root{
    --page:#cccccc;
    --green:#5a9e2a;
    --green-bright:#3fae1e;
    --green-dark:#2f7d16;
    --text:#4a4a4a;
    --muted:#b9b9b9;
    --rule:#d9e4cc;
    --white:#ffffff;
  }
  *{margin:0;padding:0;box-sizing:border-box}
  html,body{width:1200px;height:1200px;overflow:hidden}
  body{background:var(--page);font-family:'Montserrat',sans-serif;position:relative}
  .card{position:absolute;left:247px;width:712px;height:504px;overflow:hidden}
  .front{top:79px}
  .back{top:636px;background:var(--white)}

  /* front */
  .front .photo{position:absolute;inset:0;
    background:linear-gradient(180deg,#f3c47d 0%,#f0c27c 19%,#a9d6f2 22%,#cfe8f5 42%,#5e8a5a 52%,#2f9c8d 60%,#3b8a4a 70%,#c98a60 82%,#b5714c 100%)}
  .brand{position:absolute;text-align:center;color:var(--green-bright);font-weight:700;line-height:1}
  .front .brand{left:0;right:0;top:104px;font-size:40px}
  .front .brand span{display:block;font-size:18px;margin-top:8px;letter-spacing:.5px}
  .front .headline{position:absolute;left:0;right:0;top:236px;text-align:center;color:var(--white);
    font-weight:700;font-size:29px;text-shadow:0 2px 6px rgba(0,0,0,.45)}
  .front .sub{position:absolute;left:0;right:0;top:274px;text-align:center;color:var(--white);
    font-weight:500;font-size:15px;line-height:19px;text-shadow:0 1px 4px rgba(0,0,0,.5)}
  .front .rule{position:absolute;left:25px;right:25px;top:458px;height:1px;background:rgba(255,255,255,.55)}
  .front .footer{position:absolute;left:25px;right:25px;top:471px;display:flex;justify-content:space-between;
    color:var(--white);font-weight:600;font-size:10.5px;text-shadow:0 1px 3px rgba(0,0,0,.5)}
  .front .footer .contact span+span{margin-left:13px}

  /* back */
  .back .accent{position:absolute;left:0;top:0;width:25px;height:88px;background:var(--green)}
  .back .title{position:absolute;left:45px;top:32px;color:var(--green);font-weight:700;font-size:25px;line-height:31px}
  .back .intro{position:absolute;left:44px;top:100px;width:440px;color:var(--text);font-size:11.8px;line-height:16.5px}
  .services{position:absolute;left:44px;top:145px;list-style:none}
  .services li{display:flex;align-items:center;width:281px;height:26px;font-weight:600;font-size:13.5px;color:var(--text)}
  .services li+li{border-top:1px solid var(--rule)}
  .services li span{margin-left:4px}
  .services svg{width:9px;height:9px;margin-right:4px}
  .back .line{position:absolute;left:45px;width:322px;height:1px;background:var(--rule)}
  .usp-title{position:absolute;left:46px;top:262px;color:var(--green);font-weight:700;font-size:18.5px}
  .usp-text{position:absolute;left:46px;top:284px;width:280px;color:var(--text);font-size:11.8px;line-height:14.5px}
  .values{position:absolute;left:46px;top:332px;color:var(--muted);font-weight:700;font-size:18.5px;white-space:nowrap}
  .values i{display:inline-block;width:6px;height:6px;border-radius:50%;background:var(--green);margin:0 6px 0 7px;vertical-align:-1px}
  .back .brand{right:24px;top:25px;font-size:25px;text-align:center}
  .back .brand span{display:block;font-size:12px;margin-top:5px}
  .band{position:absolute;left:0;right:0;top:359px;bottom:0;
    background:linear-gradient(90deg,#3c9a1e 0%,#56b033 45%,#6ab84a 70%,#3f8f24 100%)}
  .band-text{position:absolute;left:45px;top:388px;color:var(--white)}
  .band-text h3{font-weight:700;font-size:16px;line-height:19px;margin-bottom:12px}
  .band-text p{font-size:11.3px;line-height:21.5px}
  .band-text b{font-weight:700}
  .portrait{position:absolute;left:509px;top:180px;width:203px;height:324px;
    background:linear-gradient(180deg,#f4f4f4 0%,#e9d9c9 30%,#b58a62 50%,#2a2a2a 72%,#1b1b1b 100%);
    border-radius:90px 90px 0 0}
</style>
</head>
<body>
  <section class="card front">
    <div class="photo" role="img" aria-label="Foto einer Dachterrasse mit Markise, Topfpflanzen und Blick auf den Zürichsee"></div>
    <div class="brand">Lindtaber<span>IMMOBILIEN</span></div>
    <h1 class="headline">Kostenlose Immobilienbewertung</h1>
    <p class="sub">Alles aus einer Hand – von der Bewertung bis zum Notar &amp;<br>zur Steuerberatung.</p>
    <div class="rule"></div>
    <div class="footer">
      <span>Vereinbaren Sie noch heute Ihre kostenlose Bewertung</span>
      <span class="contact"><span>Tel: +41 77 586 12 47</span><span>Mail: info@lindtaberhaus.ch</span></span>
    </div>
  </section>

  <section class="card back">
    <div class="accent"></div>
    <h2 class="title">Ihr exklusiver Immobilienpartner<br>in der Region Zürichsee</h2>
    <p class="intro">Als familiengeführtes Unternehmen mit Wurzeln in Meilen bieten wir Ihnen persönliche Betreuung, Diskretion und höchste Professionalität.</p>
    <ul class="services">
      <li><svg viewBox="0 0 10 10"><path d="M1 5.5l2.5 2.5L9 2" fill="none" stroke="#5a9e2a" stroke-width="1.4"/></svg><span>Immobilienbewertung</span></li>
      <li><svg viewBox="0 0 10 10"><path d="M1 5.5l2.5 2.5L9 2" fill="none" stroke="#5a9e2a" stroke-width="1.4"/></svg><span>Verkaufsstrategie &amp; Vermarktung</span></li>
      <li><svg viewBox="0 0 10 10"><path d="M1 5.5l2.5 2.5L9 2" fill="none" stroke="#5a9e2a" stroke-width="1.4"/></svg><span>Notariats &amp; Vertragsbegleitung</span></li>
      <li><svg viewBox="0 0 10 10"><path d="M1 5.5l2.5 2.5L9 2" fill="none" stroke="#5a9e2a" stroke-width="1.4"/></svg><span>Steuerberatung</span></li>
    </ul>
    <div class="line" style="top:255px"></div>
    <h3 class="usp-title">Alles aus einer Hand</h3>
    <p class="usp-text">von der Bewertung über den Verkauf bis zur steuerlichen Beratung.</p>
    <div class="line" style="top:320px"></div>
    <div class="values">Exklusiv<i></i>Professionell<i></i>Persönlich</div>
    <div class="brand">Lindtaber<span>IMMOBILIEN</span></div>
    <div class="band" role="img" aria-label="Grün eingefärbtes Foto einer Landschaft mit Mehrfamilienhaus"></div>
    <div class="band-text">
      <h3>Kontaktieren Sie uns für Ihre kostenlose<br>Immobilienbewertung.</h3>
      <p><b>Tel:</b> +41 77 586 12 47</p>
      <p><b>Mail:</b> info@lindtaberhaus.ch</p>
      <p><b>Web:</b> lindtaberhaus.ch</p>
    </div>
    <div class="portrait" role="img" aria-label="Porträtfoto der Ansprechpartnerin im dunklen Blazer"></div>
  </section>
</body>
</html>
```